Industrial Company Profile Brochure Design

We need company profile brochure design. We are in industrial valve business and we are serving oil, petrochemical and power plants. We are working with our clients as trusted advisor. So, the final design should communicate valve solutions expert. The brochure should be 4 pages (including front and back) or folded style. However, it is open. We do not like to put any restriction on creativity. We leave the decision for number of pages and page size to the designer. The color theme should be same as / compatible with logo colors. You should use icons.Find attached the followings:- Our Logo- Word file that contains the required content (text and photos) for the brochure.3 Modern brochure designs. We like these designs. This is just to give you idea about what we like. The brochure is simple, clear and easy to get full information quickly.- Just banner for valve and components. You may need it.

Target Market(s)

The end users of oi, petrochemical and power plants

Industry/Entity Type

Engineering Consulting

Requirements
Must have
• - You must add our slogan. It is "Your Valves Solutions Expert"

```html
<!DOCTYPE html>
<html lang="en">
<head>
<meta charset="utf-8">
<title>Nadir Hakam – Valve Solutions Brochure</title>
<link rel="stylesheet" href="https://fonts.googleapis.com/css2?family=Montserrat:wght@400;500;600;700;800&family=Roboto+Condensed:wght@400;500&display=swap">
<style>
  :root{
    --orange:#e8a33d;
    --orange-deep:#d9902a;
    --charcoal:#474747;
    --ink:#3c3c3c;
    --grey-text:#7a7a7a;
    --paper:#ffffff;
    --paper-shade:#f1f1f1;
    --band-grey:#e6e6e6;
    --stage:#d8d8d8;
  }
  *{box-sizing:border-box;margin:0;padding:0}
  html,body{width:1200px;height:789px;overflow:hidden}
  body{background:var(--stage);font-family:"Montserrat",sans-serif;color:var(--ink);position:relative}

  .sheet{position:absolute;left:20px;width:1160px;height:378px;display:flex;box-shadow:0 2px 8px rgba(0,0,0,.15)}
  .sheet--inside{top:8px}
  .sheet--outside{top:403px}
  .panel{width:290px;height:100%;background:var(--paper);position:relative;overflow:hidden;border-right:1px solid #e4e4e4}
  .panel:last-child{border-right:none}

  .icon-box{width:34px;height:28px;background:var(--orange);display:flex;align-items:center;justify-content:center}
  .icon-box svg{width:20px;height:20px;stroke:#5a4420;fill:none;stroke-width:1.4}

  .head-row{display:flex;justify-content:space-between;align-items:center}
  .title{font-weight:600;font-size:14px;color:#555}
  .title--cond{font-family:"Roboto Condensed",sans-serif;font-weight:500;font-size:13px;color:#444}

  .body{font-size:7.2px;line-height:1.32;color:#555}
  .body--large{font-size:8px;line-height:1.33}
  .body--cond{font-family:"Roboto Condensed",sans-serif;font-size:7.6px;line-height:1.35;color:#555}

  /* panel: solutions */
  .solutions{padding:16px 14px 0 14px}
  .solutions .body{margin:9px 0 10px}
  .advantages{position:absolute;left:0;right:0;bottom:0;height:96px;background:linear-gradient(90deg,var(--band-grey),#f4f4f4);padding:10px 14px}
  .advantages h3{font-weight:600;font-size:11px;line-height:1.25;color:#333}
  .advantages ul{margin:5px 0 0 30px;font-size:7.2px;line-height:1.6;color:#444}

  /* panel: values */
  .values{padding:18px 14px;background:linear-gradient(90deg,#fff,var(--paper-shade))}
  .values .body--cond{margin:9px 0 16px}

  /* panel: why choose */
  .why{padding-top:24px}
  .brand{display:flex;flex-direction:column;align-items:center;gap:6px}
  .brand-dot{width:40px;height:40px;border-radius:50%;background:var(--orange)}
  .brand-name{font-weight:700;font-size:17px;color:var(--orange);letter-spacing:.5px}
  .band{background:var(--orange);color:#2f2f2f;font-weight:700;padding:7px 14px}
  .why .band{margin-top:26px;font-size:13px;letter-spacing:.6px}
  .why h4{font-weight:600;font-size:13px;color:#333;margin:14px 16px 4px}
  .why .body{margin:0 16px}

  /* panel: about */
  .about{background:var(--paper-shade)}
  .about-photo{height:150px;background:linear-gradient(135deg,var(--orange-deep),var(--orange) 60%,#efc37a)}
  .about-card{position:absolute;left:14px;right:12px;top:76px;background:#fff;padding:12px 12px;box-shadow:0 1px 4px rgba(0,0,0,.12)}
  .about-card h3{font-family:"Roboto Condensed",sans-serif;font-weight:500;font-size:13px;color:#333;margin-bottom:4px}

  /* panel: strategy */
  .strategy{padding-top:20px}
  .strategy .band{font-size:12px;text-align:right;margin-right:18px}
  .strategy .text{padding:10px 16px 0 22px}
  .strategy .body--large+ .body--large{margin-top:8px}

  /* panels: upgrade + partners with shared photo */
  .upgrade{padding:18px 14px 0;background:linear-gradient(90deg,#f7f7f7,#ececec)}
  .upgrade ul{margin:6px 0 0 16px;font-family:"Roboto Condensed",sans-serif;font-size:7px;line-height:1.55;color:#555}
  .gasket-photo{position:absolute;top:184px;height:68px;background:linear-gradient(90deg,#b99a6c,#d8bf95 45%,#c6a97c)}
  .gasket-photo--left{left:0;right:0}
  .gasket-photo--right{left:0;right:0;top:176px}
  .upgrade .band{position:absolute;left:0;right:0;top:232px;font-family:"Roboto Condensed",sans-serif;font-weight:500;font-size:12px;padding:4px 20px}
  .upgrade .new-text{position:absolute;top:262px;left:14px;right:14px}

  .partners{padding-top:22px}
  .partners .band{text-align:center;font-size:13px}
  .partner-grid{display:grid;grid-template-columns:1fr 1fr;gap:14px 20px;padding:16px 24px 0}
  .partner-badge{height:20px;background:#d2d2d2;border-radius:3px}
  .partner-badge--round{width:38px;height:30px;border-radius:50%;background:#2c2c2c}
  .contact{position:absolute;left:16px;right:10px;top:262px}
  .contact h4{font-weight:600;font-size:10px;letter-spacing:.8px;color:#444}
  .contact .company{font-size:9px;color:var(--grey-text);margin:5px 0 6px;letter-spacing:.4px}
  .contact li{list-style:none;display:flex;gap:10px;align-items:flex-start;font-size:8px;color:#555;margin:0 0 4px 12px}
  .contact svg{width:9px;height:9px;stroke:#888;fill:none;stroke-width:1.2;flex:none;margin-top:1px}

  /* panel: cover */
  .cover{background:var(--orange)}
  .cover-top{height:150px;background:var(--charcoal);display:flex;align-items:center;justify-content:center;border-bottom:16px solid #363636}
  .cover .brand-name{font-size:18px}
  .slogan{position:absolute;left:0;right:0;top:232px;text-align:center;color:#2a2a2a;font-weight:800;line-height:1}
  .slogan .s-your{display:block;font-size:30px}
  .slogan .s-valves{display:block;font-size:30px}
  .slogan .s-expert{display:block;font-size:12px;font-weight:700;margin-top:3px}
</style>
</head>
<body>

<section class="sheet sheet--inside">
  <article class="panel solutions">
    <div class="head-row">
      <span class="icon-box"><svg viewBox="0 0 20 20"><path d="M3 13l4-2 5 1 4-4M7 6a2 2 0 1 0 4 0a2 2 0 1 0-4 0"/></svg></span>
      <h2 class="title">Our Solutions</h2>
    </div>
    <p class="body">Nadir Hakam offers a full range of consultation services to help analyze your plant requirements for the effective implementation of solutions from our range of products. We cooperate with the end-user for a detailed analysis of the root cause and provide reliable solutions for different kinds of valve problems. Our products and services could be briefly divided into the following sections:</p>
    <div class="head-row">
      <span class="icon-box"><svg viewBox="0 0 20 20"><circle cx="10" cy="10" r="4"/><path d="M10 2v3M10 15v3M2 10h3M15 10h3"/></svg></span>
      <h2 class="title">Spare Parts</h2>
    </div>
    <p class="body" style="font-size:8px">We are not only focus on providing reliable valves and upgrades, but also assist our clients in maintaining their valves. We provide direct OEM part replacements, with quality same as those originally installed. Other than providing common spare parts, we can also help in the replacement of obsolete parts not commonly available by using our trusted sources or our highly advanced reverse engineering techniques.</p>
    <div class="advantages">
      <h3>The advantages of using our parts are as follows:</h3>
      <ul>
        <li>Completely interchangeable</li>
        <li>Use of latest technology makes our parts highly durable</li>
        <li>Lower costs</li>
        <li>Faster delivery</li>
      </ul>
    </div>
  </article>

  <article class="panel values">
    <div class="head-row">
      <span class="icon-box"><svg viewBox="0 0 20 20"><rect x="5" y="4" width="10" height="12"/><path d="M7 8h6M7 11h6"/></svg></span>
      <h2 class="title--cond">Company Values</h2>
    </div>
    <p class="body--cond">At Nadir Hakam, we are committed to providing the best solutions to our clients and improving our skill sets and technology to deliver high-quality valves and valve components.</p>
    <div class="head-row">
      <span class="icon-box"><svg viewBox="0 0 20 20"><path d="M2 10c3-5 13-5 16 0c-3 5-13 5-16 0z"/><circle cx="10" cy="10" r="2.5"/></svg></span>
      <h2 class="title--cond">Our Vision</h2>
    </div>
    <p class="body--cond">To become the most trusted valve advisor in the region, maintaining the integrity and reliability of our services among our clients and partners.</p>
  </article>

  <article class="panel why">
    <div class="brand">
      <span class="brand-dot"></span>
      <span class="brand-name">NADIR HAKAM</span>
    </div>
    <div class="band">WHY CHOOSE US:</div>
    <h4>Quality Control</h4>
    <p class="body" style="font-size:8px">Our quality control processes, implemented across all stages of valve solutions, ensure consistent and reliable results for every client we serve.</p>
  </article>

  <article class="panel about">
    <div class="about-photo" role="img" aria-label="Close-up photograph of a machined valve component in warm orange light"></div>
    <div class="about-card">
      <h3>About Us</h3>
      <p class="body--cond">Nadir Hakam was established to provide highly-reliable consultation services for a selection of valve designs for various industrial applications. We specialize in recommending new valves for different types of industrial needs, as well as re-engineering the obsolete and troublesome ones, to provide technologically-advanced replacements. Our success is built on trust, expertise and long-term partnership.</p>
    </div>
  </article>
</section>

<section class="sheet sheet--outside">
  <article class="panel strategy">
    <div class="band">Strategic Approach</div>
    <div class="text">
      <p class="body body--large">The most important aspect of the solutions provided by us is that we deliver tailor-fit designs to accurately and effectively meet the needs that are not well-served by the valves currently available in the market. As in current valve manufacturing companies, the engineers are limited to providing standard designs created by their companies.</p>
      <p class="body body--large">This also limits them from fulfilling any type of modification requirement. For this reason, there are many valve problems that cannot be solved by standard designs. Furthermore, the parts replacements provided by us meet the requirements and come at a much lower cost, as compared to the parts delivered by these manufacturers.</p>
      <p class="body body--large">We are open and cooperate with several trusted companies to find the best solutions for the end-user problems by providing detailed analysis and consultation services, helping them to buy the most relevant products as per their needs. We aim to be the best choice in valve consultation.</p>
    </div>
  </article>

  <article class="panel upgrade">
    <h2 class="title--cond">Upgrade &amp; Retrofit</h2>
    <p class="body--cond" style="font-size:6.8px">We supply highly reliable and efficient upgrading solutions for our clients, with the following</p>
    <h3 class="title--cond" style="font-size:12px;margin-top:4px">key advantages:</h3>
    <ul>
      <li>Fits well into the existing valve</li>
      <li>Full responsibility of the valve</li>
      <li>Detailed documentation</li>
      <li>Saves the cost of piping modifications</li>
      <li>Lower installation costs</li>
      <li>Shorter plant downtime</li>
    </ul>
    <div class="gasket-photo gasket-photo--left" style="height:48px" role="img" aria-label="Photograph of spiral wound valve gaskets"></div>
    <div class="band">New Valves</div>
    <p class="body--cond new-text">We provide consultation on and design of a variety of valves for different kinds of industrial applications. We have a rich set of valve designs and solutions available, providing solutions for severe service applications. For special valve solutions not available in the market, we can help our clients by manufacturing and delivering those valves in the shortest possible time-frame under the most complicated requirements.</p>
  </article>

  <article class="panel partners">
    <div class="band">Our Partners:</div>
    <div class="partner-grid">
      <span class="partner-badge partner-badge--round"></span>
      <span class="partner-badge"></span>
      <span class="partner-badge"></span>
      <span class="partner-badge"></span>
    </div>
    <div class="gasket-photo gasket-photo--right" role="img" aria-label="Photograph of spiral wound valve gaskets, continued"></div>
    <div class="contact">
      <h4>CONTACT DETAILS:</h4>
      <p class="company">Nadir Hakam</p>
      <ul>
        <li><svg viewBox="0 0 10 10"><path d="M2 1l2 2-1 1c1 1.5 2 2.5 3 3l1-1 2 2-1.5 1.5C4 9 1 6 .5 2.5z"/></svg>+966 500 000 111</li>
        <li><svg viewBox="0 0 10 10"><path d="M5 9.5S1.5 6 1.5 4a3.5 3.5 0 0 1 7 0C8.5 6 5 9.5 5 9.5z"/><circle cx="5" cy="4" r="1.2"/></svg>Sahil Rd - Harbor City<br>10000</li>
        <li><svg viewBox="0 0 10 10"><rect x=".7" y="2" width="8.6" height="6"/><path d="M.7 2l4.3 3.4L9.3 2"/></svg>info@nadirhakam.example</li>
        <li><svg viewBox="0 0 10 10"><circle cx="5" cy="5" r="4.2"/><path d="M.8 5h8.4M5 .8c-2 2.5-2 5.9 0 8.4M5 .8c2 2.5 2 5.9 0 8.4"/></svg>www.nadirhakam.example</li>
      </ul>
    </div>
  </article>

  <article class="panel cover">
    <div class="cover-top">
      <div class="brand">
        <span class="brand-dot"></span>
        <span class="brand-name">NADIR HAKAM</span>
      </div>
    </div>
    <p class="slogan">
      <span class="s-your">YOUR</span>
      <span class="s-valves">Valves</span>
      <span class="s-expert">Solutions Expert</span>
    </p>
  </article>
</section>

</body>
</html>
```